Mortgage Broking boutique Business

I’m wanting a revamped look to my existing business card design. I do like the black and silver but happy to have other colours introduced based on your creation. I’ve attached a copy of my current card so you can have a starting point updated details noted brloe. I deal with high net worth individuals so need my card to be sophisticated, classy that gives off a classy vibe

Target Market(s)

High net worth, wealthy

Industry/Entity Type

Mortgage Brokerage

Contact Information for Business Card

Job title: Finance Executive
Phone: +61 7 3287 4419
Mobile: 0471 352 608
Email: marcus@quillbrookcapital.com.au
Web: www.quillbrookcapital.com.au
Address: level 36 Tindale Court, 58 Harwick St Brisbane QLD 4000

Font styles to use
Other font styles liked:
• Helvetica

Colors

Designer to choose colors to be used in the design.

Requirements
Must have
• Use my existing card design as a starting point

```html
<!DOCTYPE html>
<html lang="en">
<head>
<meta charset="utf-8">
<title>Quillbrook Capital – Business Card</title>
<link rel="stylesheet" href="https://fonts.googleapis.com/css2?family=Jost:wght@400&family=Source+Sans+3:wght@400;600&display=swap">
<style>
  :root {
    --backdrop: #6b6b6b;
    --card: #151515;
    --card-edge: #0e0e0e;
    --text: #d6d6d6;
    --accent: #e4441d;
    --silver-light: #f4f4f4;
    --silver-mid: #9a9a9a;
    --silver-dark: #3a3a3a;
  }
  * { margin: 0; padding: 0; box-sizing: border-box; }
  html, body { width: 1200px; height: 802px; overflow: hidden; }
  body { background: var(--backdrop); position: relative; font-family: "Source Sans 3", sans-serif; }

  .card {
    position: absolute; top: 274px; width: 443px; height: 265px;
    background: var(--card); overflow: hidden;
    box-shadow: 2px 3px 6px rgba(0,0,0,.45);
  }
  .card--front { left: 136px; }
  .card--back { left: 624px; }

  .silver-band {
    position: absolute; left: 0; top: 0; width: 59px; height: 100%;
    background: linear-gradient(180deg, #1a1a1a 0%, #5a5a5a 25%, var(--silver-light) 50%, #6a6a6a 75%, #1a1a1a 100%);
  }
  .silver-rule {
    position: absolute; left: 63px; top: 0; width: 2px; height: 100%;
    background: linear-gradient(180deg, #333, #bbb 50%, #333);
  }

  .brand-plate { position: absolute; }
  .brand-plate svg { position: absolute; inset: 0; }
  .brand-plate__name {
    position: absolute; inset: 0; display: flex; flex-direction: column;
    align-items: center; justify-content: center;
    font-family: "Jost", sans-serif; font-weight: 400; color: var(--text);
    text-transform: uppercase; text-align: center;
  }
  .card--front .brand-plate { left: 224px; top: 31px; width: 184px; height: 95px; }
  .card--front .brand-plate__name { font-size: 11.5px; letter-spacing: 3px; line-height: 14px; }
  .card--back .brand-plate { left: 30px; top: 37px; width: 377px; height: 194px; }
  .card--back .brand-plate__name { font-size: 23px; letter-spacing: 6px; line-height: 28px; }

  .holder { position: absolute; left: 86px; top: 99px; }
  .holder__name { font-size: 17px; font-weight: 600; color: var(--accent); line-height: 20px; }
  .holder__title { font-size: 12.5px; color: var(--text); line-height: 14px; }

  .contact-list { position: absolute; left: 86px; top: 139px; list-style: none; }
  .contact-list li {
    display: flex; align-items: center; height: 15.8px;
    font-size: 12.5px; color: var(--text);
  }
  .contact-list svg { width: 10px; height: 10px; margin-right: 5px; fill: var(--accent); }

  .address {
    position: absolute; left: 86px; top: 210px;
    font-size: 12.5px; line-height: 15.8px; color: var(--text); font-style: normal;
  }
</style>
</head>
<body>

<svg width="0" height="0" style="position:absolute">
  <defs>
    <linearGradient id="silver" x1="0" y1="0" x2="1" y2="1">
      <stop offset="0" stop-color="#8c8c8c"/>
      <stop offset=".3" stop-color="#e8e8e8"/>
      <stop offset=".55" stop-color="#7a7a7a"/>
      <stop offset=".8" stop-color="#dcdcdc"/>
      <stop offset="1" stop-color="#8a8a8a"/>
    </linearGradient>
    <radialGradient id="plate-glow" cx=".5" cy=".5" r=".6">
      <stop offset="0" stop-color="#3a3a3a"/>
      <stop offset="1" stop-color="#121212"/>
    </radialGradient>
  </defs>
</svg>

<section class="card card--front" aria-label="Card front">
  <div class="silver-band"></div>
  <div class="silver-rule"></div>

  <div class="brand-plate">
    <svg viewBox="0 0 184 95" preserveAspectRatio="none">
      <rect x="0" y="0" width="184" height="95" fill="url(#plate-glow)"/>
      <rect x="1.5" y="1.5" width="181" height="92" fill="none" stroke="url(#silver)" stroke-width="3"/>
      <rect x="6" y="6" width="172" height="83" fill="none" stroke="url(#silver)" stroke-width="1.5"/>
    </svg>
    <div class="brand-plate__name"><span>Quillbrook</span><span>Capital</span></div>
  </div>

  <div class="holder">
    <p class="holder__name">MARCUS THORNE</p>
    <p class="holder__title">Finance Executive</p>
  </div>

  <ul class="contact-list">
    <li><svg viewBox="0 0 10 10"><path d="M1 3.5 Q5 0.5 9 3.5 L8 5 L6.5 4.2 L6.5 3.3 Q5 2.8 3.5 3.3 L3.5 4.2 L2 5 Z M2.5 5.5 H7.5 L8.5 9 H1.5 Z"/></svg>+61 7 3287 4419</li>
    <li><svg viewBox="0 0 10 10"><path d="M3 0.5 H7 Q7.8 0.5 7.8 1.3 V8.7 Q7.8 9.5 7 9.5 H3 Q2.2 9.5 2.2 8.7 V1.3 Q2.2 0.5 3 0.5 Z M3.2 1.6 V7.6 H6.8 V1.6 Z"/></svg>0471 352 608</li>
    <li><svg viewBox="0 0 10 10"><path d="M0.5 2 H9.5 V8 H0.5 Z M1.2 2.6 L5 5.5 L8.8 2.6 Z" fill-rule="evenodd"/></svg>marcus@quillbrookcapital.com.au</li>
    <li><svg viewBox="0 0 10 10"><circle cx="5" cy="5" r="4.5"/></svg>www.quillbrookcapital.com.au</li>
  </ul>

  <address class="address">level 36 Tindale Court,<br>58 Harwick St Brisbane QLD 4000</address>
</section>

<section class="card card--back" aria-label="Card back">
  <div class="brand-plate">
    <svg viewBox="0 0 377 194" preserveAspectRatio="none">
      <rect x="0" y="0" width="377" height="194" fill="url(#plate-glow)"/>
      <rect x="2.5" y="2.5" width="372" height="189" fill="none" stroke="url(#silver)" stroke-width="5"/>
      <rect x="11" y="11" width="355" height="172" fill="none" stroke="url(#silver)" stroke-width="3"/>
    </svg>
    <div class="brand-plate__name"><span>Quillbrook</span><span>Capital</span></div>
  </div>
</section>

</body>
</html>
```